i need a business card design for my family investment company "norvane holdings" based in dubai. its a diverse investment firm focusing on education, hospitality and automotive. the design has to be modern and try to incorporate the logo "E" in the design. details on card as follow

Tariq H Bin Rashoud
Managing Director
tariq@norvane.ae
www.norvane.ae

Harbor park,palmcrest tower, office 1730, dubai
tel. 04 3819025
mobile.050 4172958

Target Market(s)

card used for networking events and investor meetings

Industry/Entity Type

Hospitality

```html
<!DOCTYPE html>
<html lang="en">
<head>
<meta charset="utf-8">
<title>Norvane Holdings – Business Card</title>
<link rel="stylesheet" href="https://fonts.googleapis.com/css2?family=Cinzel:wght@400;700&display=swap">
<style>
  :root {
    --bg: #e4e4e4;
    --paper: #f7f7f6;
    --ink: #1b1b1b;
    --steel: #44698d;
    --steel-light: #5b7e9b;
    --steel-dark: #2e5176;
    --black: #050505;
    --white: #ffffff;
  }
  * { box-sizing: border-box; margin: 0; padding: 0; }
  html, body { width: 1200px; height: 720px; overflow: hidden; }
  body {
    background: var(--bg);
    font-family: "Cinzel", serif;
    position: relative;
  }
  .card {
    position: absolute;
    top: 242px;
    width: 420px;
    height: 239px;
    overflow: hidden;
    box-shadow: 0 3px 8px rgba(0,0,0,0.18);
  }
  /* Front */
  .card-front { left: 147px; background: var(--paper); color: var(--ink); }
  .brand {
    position: absolute; left: 23px; top: 22px;
    color: var(--ink); font-weight: 400; line-height: 1;
  }
  .brand-name { display: block; font-size: 25px; letter-spacing: 11px; }
  .brand-sub { display: block; font-size: 9px; letter-spacing: 8.6px; margin-top: 7px; }
  .holder { position: absolute; left: 23px; top: 86px; }
  .holder-name { font-size: 13px; font-weight: 700; color: var(--steel); line-height: 1.1; }
  .holder-title { font-size: 9.5px; line-height: 1.2; }
  .address { position: absolute; left: 23px; top: 126px; font-size: 9.5px; line-height: 12.5px; }
  .contacts { position: absolute; left: 23px; top: 166px; list-style: none; }
  .contacts li {
    display: flex; align-items: center; height: 12px;
    font-size: 9.5px; line-height: 12px;
  }
  .contacts svg { width: 10px; height: 10px; margin-right: 11px; fill: var(--steel-dark); flex: none; }
  .footer-bands { position: absolute; left: 0; bottom: 0; width: 420px; height: 22px; }
  /* Back */
  .card-back {
    left: 633px;
    background: linear-gradient(135deg, var(--steel-light) 0%, var(--steel) 50%, var(--steel-dark) 100%);
    color: var(--white);
  }
  .edge-tab { position: absolute; left: 0; width: 58px; height: 14px; background: var(--white); }
  .edge-tab.top { top: 0; }
  .edge-tab.middle { top: 101px; }
  .edge-tab.bottom { bottom: 0; }
  .brand-back {
    position: absolute; left: 104px; top: 88px;
    color: var(--white); font-weight: 400; line-height: 1;
  }
  .brand-back .brand-name { font-size: 38px; letter-spacing: 14px; }
  .brand-back .brand-sub { font-size: 12px; letter-spacing: 13px; margin-top: 10px; }
</style>
</head>
<body>
  <section class="card card-front">
    <div class="brand">
      <span class="brand-name">NORVANE</span>
      <span class="brand-sub">HOLDINGS</span>
    </div>
    <div class="holder">
      <p class="holder-name">Tariq H Bin Rashoud</p>
      <p class="holder-title">Managing Director</p>
    </div>
    <p class="address">Harbor park, palmcrest tower,<br>office 1730, dubai</p>
    <ul class="contacts">
      <li><svg viewBox="0 0 10 10"><path d="M0 4c0-2 2-3 5-3s5 1 5 3v1H7V4H3v1H0z M2 5h6l1 4H1z"/></svg>04 3819025</li>
      <li><svg viewBox="0 0 10 10"><path d="M2.5 0h5v10h-5z M3.5 1v7h3V1z" fill-rule="evenodd"/></svg>050 4172958</li>
      <li><svg viewBox="0 0 10 10"><path d="M0 2h10v6H0z M1 3l4 3 4-3" fill-rule="evenodd"/><path d="M1 3l4 3 4-3" stroke="#f7f7f6" stroke-width="0.8" fill="none"/></svg>tariq@norvane.ae</li>
      <li><svg viewBox="0 0 10 10"><path d="M0 1h10v6H0z M1 2v4h8V2z M4 7h2v1.5h2V9H2v-.5h2z" fill-rule="evenodd"/></svg>www.norvane.ae</li>
    </ul>
    <svg class="footer-bands" viewBox="0 0 420 22" preserveAspectRatio="none" aria-hidden="true">
      <polygon points="0,10 303,10 297,22 0,22" fill="var(--black)"/>
      <polygon points="315,0 420,0 420,22 302,22" fill="var(--steel)"/>
    </svg>
  </section>

  <section class="card card-back">
    <span class="edge-tab top"></span>
    <span class="edge-tab middle"></span>
    <span class="edge-tab bottom"></span>
    <div class="brand-back">
      <span class="brand-name">NORVANE</span>
      <span class="brand-sub">HOLDINGS</span>
    </div>
  </section>
</body>
</html>
```